Business Card for Polygraph business in Africa

Business Card . Polygraph Examiner based in Tanzania, East Africa.
Business Card will be used to disseminate contact information to potential clients.
It should convey that I am a professional specifically in the polygraph field and perform my work with integrity.

I have attached the business card that I'm currently using, which I threw together myself initially. It's not professional enough.

Target Market(s)

Banks, Accounting Firms, Government Ministries, Gas, Oil, & Gemstone Mining Concerns, Wildlife Conservation NGOs, International companies located in East Africa.

Industry/Entity Type

Business

Contact Information for Business Card

Veritrace Kilanga
Miriam Ostbrook
PO Box 48731
Arusha, Tanzania
+255 684 219 537
miriamostbrook@mailvera.example

Colors
00a990
f37122
faa54b

Requirements
Must have
• - Veritrace Kilanga (with the word "Polygraph" being more prominent than the word "Tanzania")
• - Forensic Examinations
• - Employment Screening
• - Should contain a logo of the Continental Truthtrace Society (of which I'm a member)
• - I would like an accent design (such as the polygraph "squiggles" of a cardio tracing or such as that)
• - My contact information (less prominent, but large enough to read legibly). I would also consider putting the contact information on the second side of the card.
Nice to have
• My color suggestions are changeable.
Should not have
• Anything "cutesy" or "cartoonish"

```html
<!DOCTYPE html>
<html lang="en">
<head>
<meta charset="utf-8">
<title>Veritrace Kilanga – Business Card</title>
<link rel="stylesheet" href="https://fonts.googleapis.com/css2?family=Raleway:wght@500&family=Source+Sans+3:wght@400&display=swap">
<style>
  :root {
    --stage: #3a3a3a;
    --card: #262626;
    --brand-grey: #9c9c9c;
    --text-grey: #a8a8a8;
    --teal: #14a08a;
    --orange: #e0762a;
    --badge: #d8d8d8;
  }
  * { margin: 0; padding: 0; box-sizing: border-box; }
  html, body { width: 1200px; height: 716px; overflow: hidden; }
  body {
    background: var(--stage);
    position: relative;
    font-family: "Source Sans 3", Arial, sans-serif;
  }
  .card {
    position: absolute;
    width: 520px;
    height: 298px;
    background: var(--card);
    border-radius: 4px;
    box-shadow: 0 6px 18px rgba(0,0,0,.45);
    overflow: hidden;
  }
  .card--front { left: 50px; top: 60px; }
  .card--back  { left: 630px; top: 60px; }

  .brand-name {
    font-family: "Raleway", Arial, sans-serif;
    font-weight: 500;
    color: var(--brand-grey);
    white-space: nowrap;
  }
  .card--front .brand-name {
    position: absolute; left: 60px; top: 100px; font-size: 34px;
  }
  .member-badge {
    position: absolute; right: 40px; top: 70px;
    width: 80px; height: 80px;
  }
  .services {
    position: absolute; left: 60px; bottom: 56px;
    font-size: 16px; color: var(--text-grey); letter-spacing: .2px;
  }
  .services .divider { margin: 0 14px; }

  .card--back .brand-name {
    position: absolute; left: 28px; top: 128px; font-size: 22px;
  }
  .rule {
    position: absolute; left: 232px; top: 40px;
    width: 2px; height: 218px; background: var(--orange);
  }
  .contact {
    position: absolute; left: 254px; top: 58px;
    color: var(--text-grey); font-size: 14px; line-height: 1.35;
  }
  .contact__name { font-size: 21px; margin-bottom: 18px; }
  .contact__row { display: flex; gap: 9px; margin-bottom: 8px; white-space: nowrap; }
  .contact__row svg { flex: none; width: 14px; height: 14px; margin-top: 2px; fill: var(--teal); }

  .lockup {
    position: absolute; left: 50px; top: 560px;
    font-size: 62px;
  }
</style>
</head>
<body>
  <section class="card card--front">
    <div class="brand-name">Veritrace Kilanga</div>
    <svg class="member-badge" viewBox="0 0 86 86" role="img" aria-label="Continental Truthtrace Society membership badge">
      <circle cx="43" cy="43" r="41" fill="none" stroke="var(--badge)" stroke-width="3"/>
    </svg>
    <p class="services">Issue investigation<span class="divider">/</span>Employment screening</p>
  </section>

  <section class="card card--back">
    <div class="brand-name">Veritrace Kilanga</div>
    <div class="rule"></div>
    <div class="contact">
      <p class="contact__name">Miriam Ostbrook</p>
      <div class="contact__row">
        <svg viewBox="0 0 14 14" aria-hidden="true"><path d="M7 0a5 5 0 0 0-5 5c0 3.6 5 9 5 9s5-5.4 5-9a5 5 0 0 0-5-5zm0 7a2 2 0 1 1 0-4 2 2 0 0 1 0 4z"/></svg>
        <span>PO Box 48731<br>Arusha, Tanzania</span>
      </div>
      <div class="contact__row">
        <svg viewBox="0 0 14 14" aria-hidden="true"><path d="M1 4c0-1.5 2.5-3 6-3s6 1.5 6 3v1.5H10V4H4v1.5H1zM3 6h8l2 4v3H1v-3zm4 1.5a2 2 0 1 0 0 4 2 2 0 0 0 0-4z"/></svg>
        <span>+255 684 219 537</span>
      </div>
      <div class="contact__row">
        <svg viewBox="0 0 14 14" aria-hidden="true"><path d="M0 3h14v8H0zm1 1v.4l6 3.6 6-3.6V4z"/></svg>
        <span>miriamostbrook@mailvera.example</span>
      </div>
    </div>
  </section>

  <div class="brand-name lockup">Veritrace Kilanga</div>
</body>
</html>
```